Plumhart honey labels

we are in need of new labels. we are changing to shorter round cream style honey jars. scalable from 25-100mm tall. We are looking for simple yet elegant
we sell premium varietal honeys from around the USA and locally produced small batch honeys. we are in San Francisco and Sonoma county Calif. for 10 yrs. we strive to supply only the highest quality honey at a premium price point
our logo is gold text on black background, can be found at plumhart.net

Reason: would like to see more designs for a paper wrap around label

Reason: get your designs in so we can choose soon

Target Market(s)

we provide Premium honeys that cannot be found easily elsewhere
at Premium prices. Our customers are socially aware but not afraid to pay more for a premium product

Colors

Designer to choose colors to be used in the design.

Requirements
Must have
• we will be using round jars in 3 sizes, 1.5-4 inches tall, 53mm,63mm,89mm diameter
all will have black lids
will need wrap around labels for labeling machine application
will need simple nutrition label info included
Nice to have
• room on side for nutrition label info
plumhart logo included, of course
space on side for short description of honey
Should not have
• honey dripping off honey dipper or spoon
picture of honeycomb
comic bees or flowers

```html
<!DOCTYPE html>
<html lang="en">
<head>
<meta charset="utf-8">
<title>Plumhart honey wrap label</title>
<link rel="stylesheet" href="https://fonts.googleapis.com/css2?family=Saira+Extra+Condensed:wght@300;500;700&family=Bebas+Neue&display=swap">
<style>
  :root {
    --label-yellow: #FFC805;
    --ink: #0A0A0A;
    --placeholder-bee: #E8B300;
    --placeholder-comb: #FFF6D2;
  }
  html, body {
    margin: 0;
    padding: 0;
    width: 1200px;
    height: 4784px;
    overflow: hidden;
    background: var(--label-yellow);
  }
  .label {
    position: relative;
    width: 1200px;
    height: 4784px;
    background: var(--label-yellow);
  }
  .bee-illustration {
    position: absolute;
    left: 150px;
    top: 180px;
    width: 310px;
    height: 240px;
    border-radius: 48px;
    background: var(--placeholder-bee);
  }
  .wordmark {
    position: absolute;
    left: 0;
    top: 0;
    width: 1200px;
    height: 4784px;
  }
  .wordmark text {
    font-family: "Saira Extra Condensed", "Arial Narrow", sans-serif;
    font-weight: 300;
    fill: var(--ink);
  }
  .comb-illustration {
    position: absolute;
    left: 200px;
    top: 3000px;
    width: 800px;
    height: 800px;
    border-radius: 60px;
    background: var(--placeholder-comb);
  }
  .nutrition {
    position: absolute;
    left: 240px;
    top: 3880px;
    width: 720px;
    box-sizing: border-box;
    border: 8px solid var(--ink);
    padding: 14px 28px 18px;
    font-family: "Saira Extra Condensed", "Arial Narrow", sans-serif;
    color: var(--ink);
  }
  .nutrition-title {
    margin: 0;
    font-weight: 700;
    font-size: 84px;
    line-height: 1;
    border-bottom: 4px solid var(--ink);
    padding-bottom: 8px;
  }
  .nutrition-serving {
    margin: 8px 0 0;
    font-weight: 500;
    font-size: 38px;
    line-height: 1.15;
    border-bottom: 14px solid var(--ink);
    padding-bottom: 8px;
  }
  .nutrition-row {
    display: flex;
    justify-content: space-between;
    margin: 0;
    font-weight: 500;
    font-size: 38px;
    line-height: 1.3;
    border-bottom: 3px solid var(--ink);
  }
  .nutrition-row.calories {
    font-weight: 700;
    font-size: 52px;
    border-bottom-width: 8px;
  }
  .nutrition-row:last-child { border-bottom: none; }
  .volume {
    position: absolute;
    left: 0;
    width: 1200px;
    top: 4550px;
    margin: 0;
    text-align: center;
    font-family: "Bebas Neue", "Oswald", sans-serif;
    font-size: 150px;
    line-height: 1;
    color: var(--ink);
    letter-spacing: 2px;
  }
</style>
</head>
<body>
  <main class="label">
    <div class="bee-illustration" role="img" aria-label="Small line drawing of a bee"></div>

    <svg class="wordmark" viewBox="0 0 1200 4784" aria-label="plumhart">
      <text transform="translate(920 2850) rotate(-90)" font-size="1000" textLength="2330" lengthAdjust="spacingAndGlyphs">plumhart</text>
    </svg>

    <div class="comb-illustration" role="img" aria-label="Cluster of three outlined hexagon cells"></div>

    <section class="nutrition" aria-label="Nutrition facts">
      <h2 class="nutrition-title">Nutrition Facts</h2>
      <p class="nutrition-serving">Serving size 1 tbsp (21g)</p>
      <p class="nutrition-row calories"><span>Calories</span><span>60</span></p>
      <p class="nutrition-row"><span>Total Fat 0g</span><span>Sodium 0mg</span></p>
      <p class="nutrition-row"><span>Total Carbohydrate 17g</span><span>6%</span></p>
      <p class="nutrition-row"><span>Total Sugars 17g</span><span>Protein 0g</span></p>
    </section>

    <p class="volume">250ML</p>
  </main>
</body>
</html>
```